Local Computer Repair Business needs Flyer Design

I am looking for a small postcard sized (4x6) advertisement but use the full space 4x6. We are a local computer repair shop that provide sales and service of computer systems, any models, any problems. We also offer E-cycling for our customers. This will be distributed via post office box.
Emphasize shop locally, best service around, professional, Competitive prices.
One side for computer sales/repair and the other side should be E-Cycling. we'll receive old laptops, desktop computers, tablets, game consoles, etc..
Ad must include the attached logo.
Ad must include address - 872 Larkspur Ave. Hudson, IA 50619
Ad must include phone number and website - 319-555-0174 and www.quillbyrnservices.com

```html
<!DOCTYPE html>
<html lang="en">
<head>
<meta charset="utf-8">
<title>Quillbyrn Services Postcard</title>
<link href="https://fonts.googleapis.com/css2?family=Audiowide&family=Source+Sans+3:wght@400;600;700&display=swap" rel="stylesheet">
<style>
  :root {
    --navy: #2b3d9b;
    --navy-deep: #0c1d36;
    --sky: #1e9be0;
    --cyan: #1aa6e6;
    --yellow: #f7d117;
    --charcoal: #353539;
    --red: #e8202a;
    --white: #ffffff;
    --ink: #1a1a1a;
    --link: #2b3d9b;
    --stage: #d8d8d8;
  }
  * { box-sizing: border-box; margin: 0; padding: 0; }
  html, body { width: 960px; height: 1200px; overflow: hidden; }
  body {
    background: var(--stage);
    font-family: "Source Sans 3", sans-serif;
    position: relative;
  }
  .postcard {
    position: absolute;
    left: 125px;
    width: 713px;
    height: 474px;
    overflow: hidden;
    background: var(--white);
  }
  .postcard--repair { top: 70px; }
  .postcard--ecycling { top: 650px; }
  .shapes { position: absolute; inset: 0; width: 713px; height: 474px; }
  .abs { position: absolute; }

  .brand {
    font-family: "Source Sans 3", sans-serif;
    font-weight: 700;
    color: var(--navy);
    font-size: 19px;
    letter-spacing: 1.5px;
    line-height: 1.05;
    display: flex;
    align-items: center;
    gap: 8px;
  }
  .brand-dot { width: 14px; height: 14px; border-radius: 50%; background: var(--navy); flex: none; }

  /* Repair side */
  .contact-block {
    right: 19px; top: 10px;
    text-align: right;
    font-size: 13px;
    line-height: 17.5px;
    color: var(--ink);
  }
  .contact-block .phone { color: var(--link); }
  .contact-block .web-accent { color: var(--link); }
  .intro {
    left: 25px; top: 44px; width: 230px;
    color: var(--white);
    font-size: 16px;
    line-height: 20px;
  }
  .intro .highlight { color: var(--yellow); font-weight: 600; }
  .intro .big { color: var(--yellow); font-size: 21px; line-height: 26px; }
  .intro p + p { margin-top: 14px; }
  .checklist {
    left: 20px; top: 296px;
    list-style: none;
    font-family: "Audiowide", sans-serif;
    color: var(--white);
    font-size: 19px;
    line-height: 24px;
  }
  .checklist li { display: flex; align-items: center; gap: 8px; }
  .checklist svg { width: 16px; height: 16px; flex: none; }
  .slogan {
    left: 24px; top: 408px;
    font-family: "Audiowide", sans-serif;
    color: var(--white);
    font-size: 22px;
    line-height: 26px;
    letter-spacing: 0.5px;
  }

  /* E-cycling side */
  .ecycle-title {
    left: 28px; top: 90px;
    font-family: "Audiowide", sans-serif;
    color: var(--yellow);
    font-size: 33px;
  }
  .ecycle-copy {
    left: 30px; top: 145px;
    color: var(--white);
    font-size: 16px;
    line-height: 20px;
  }
  .services-heading {
    left: 30px; top: 206px;
    color: var(--white);
    font-size: 16px;
  }
  .service {
    position: absolute;
    top: 254px;
    height: 108px;
  }
  .service-photo {
    width: 100%; height: 100%;
    clip-path: polygon(8% 0, 100% 0, 92% 100%, 0 100%);
  }
  .service-label {
    position: absolute;
    top: 132px;
    left: 0; right: 0;
    text-align: center;
    color: var(--white);
    font-size: 15px;
  }
  .footer-info {
    left: 26px; top: 418px;
    color: var(--white);
    font-size: 15px;
    line-height: 25px;
  }
  .footer-info div { display: flex; align-items: center; gap: 12px; }
  .footer-info svg { width: 16px; height: 16px; flex: none; }
  .footer-phone {
    left: 324px; top: 420px;
    display: flex; align-items: center; gap: 20px;
    color: var(--white);
    font-weight: 700;
    font-size: 37px;
  }
  .footer-phone svg { width: 44px; height: 44px; }
</style>
</head>
<body>

<section class="postcard postcard--repair">
  <svg class="shapes" viewBox="0 0 713 474" aria-hidden="true">
    <rect width="713" height="474" fill="var(--white)"/>
    <polygon points="0,0 204,0 408,392 0,392" fill="var(--navy)"/>
    <polygon points="180,0 204,0 392,328 368,328" fill="var(--sky)"/>
    <polygon points="0,0 60,0 84,30 0,30" fill="var(--sky)"/>
    <rect x="0" y="250" width="176" height="10" fill="#e4e4e4"/>
    <rect x="0" y="262" width="210" height="8" fill="var(--sky)"/>
    <polygon points="0,392 572,392 612,468 0,468" fill="var(--charcoal)"/>
    <rect x="0" y="468" width="713" height="6" fill="var(--red)"/>
    <polyline points="306,0 354,90" stroke="var(--white)" stroke-width="2" fill="none"/>
  </svg>
  <div class="abs" role="img" aria-label="Photo of a technician's hand pulling a component from an open desktop tower full of cables"
       style="left:0;top:0;width:713px;height:474px;clip-path:polygon(248px 84px,713px 84px,713px 474px,612px 468px,572px 392px,408px 392px);background:linear-gradient(120deg,#cfcfcf 0%,#8f8a86 35%,#5b4f4a 60%,#8c2c32 75%,#d7d7d7 100%);"></div>
  <svg class="shapes" viewBox="0 0 713 474" aria-hidden="true">
    <rect x="612" y="462" width="101" height="6" fill="var(--navy)"/>
    <polygon points="0,464 616,464 618,468 0,468" fill="var(--charcoal)"/>
    <polygon points="210,304 244,304 262,320 228,320" fill="var(--sky)"/>
    <polygon points="236,322 270,322 286,336 252,336" fill="var(--cyan)"/>
    <polygon points="340,338 380,338 396,358 356,358" fill="var(--sky)"/>
  </svg>

  <div class="abs brand" style="left:255px;top:30px;">
    <span class="brand-dot"></span>
    <span>QUILLBYRN<br>SERVICES, LLC.</span>
  </div>
  <div class="abs contact-block">
    <div>872 Larkspur Ave. Hudson,</div>
    <div>IA 50619</div>
    <div class="phone">319-555-0174</div>
    <div>www.<span class="web-accent">quillbyrnservices</span>.com</div>
  </div>

  <div class="abs intro">
    <p>We are a local<br><span class="highlight">COMPUTER REPAIR</span><br>shop that provide sales and service of computer systems, <span class="big">ANY Models,<br>ANY Problems.</span></p>
    <p>We also offer <span class="big">E-cycling</span><br>for our customers.</p>
  </div>

  <ul class="abs checklist">
    <li><svg viewBox="0 0 16 16"><circle cx="8" cy="8" r="6.5" fill="none" stroke="var(--yellow)" stroke-width="1.5"/><path d="M4.5 8 L7.5 11 L14 3" fill="none" stroke="var(--yellow)" stroke-width="2"/></svg>Best service around</li>
    <li><svg viewBox="0 0 16 16"><circle cx="8" cy="8" r="6.5" fill="none" stroke="var(--yellow)" stroke-width="1.5"/><path d="M4.5 8 L7.5 11 L14 3" fill="none" stroke="var(--yellow)" stroke-width="2"/></svg>Professional</li>
    <li><svg viewBox="0 0 16 16"><circle cx="8" cy="8" r="6.5" fill="none" stroke="var(--yellow)" stroke-width="1.5"/><path d="M4.5 8 L7.5 11 L14 3" fill="none" stroke="var(--yellow)" stroke-width="2"/></svg>Competitive prices</li>
  </ul>

  <div class="abs slogan">SOLUTIONS TO ALL YOUR<br>TECHNOLOGY NEEDS.</div>
</section>

<section class="postcard postcard--ecycling">
  <svg class="shapes" viewBox="0 0 713 474" aria-hidden="true">
    <rect width="713" height="474" fill="var(--navy-deep)"/>
    <polygon points="0,0 440,0 448,84 0,84" fill="var(--white)"/>
    <polygon points="318,0 713,0 713,212 448,212" fill="var(--white)"/>
    <polygon points="318,0 340,0 450,212 428,212" fill="var(--navy)"/>
    <polygon points="0,140 430,140 440,190 0,190" fill="#1f5f9e" opacity="0.85"/>
    <polygon points="0,196 470,196 484,232 0,232" fill="var(--cyan)"/>
    <polygon points="0,407 780,407 760,474 0,474" fill="var(--navy)"/>
    <polygon points="780,407 713,407 713,474 760,474" fill="var(--navy)"/>
    <polygon points="771,440 713,440 713,474 765,474" fill="var(--red)"/>
    <polygon points="650,407 656,407 640,474 634,474" fill="var(--white)"/>
    <polygon points="644,440 713,440 713,474 636,474" fill="var(--red)"/>
  </svg>

  <div class="abs brand" style="left:42px;top:22px;">
    <span class="brand-dot"></span>
    <span>QUILLBYRN<br>SERVICES, LLC.</span>
  </div>

  <div class="abs" role="img" aria-label="Recycling arrows textured with green circuit board"
       style="left:462px;top:24px;width:182px;height:182px;border-radius:50%;background:radial-gradient(circle,#ffffff 28%,#2f9a3a 30%,#14571d 70%,#ffffff 72%);"></div>

  <div class="abs ecycle-title">E-Cycling</div>
  <div class="abs ecycle-copy">We'll receive Old Laptops, Desktop computers,<br>Tablets, Game consoles, etc..</div>
  <div class="abs services-heading">Here are a few of the Servcies we provide</div>

  <div class="service" style="left:11px;width:164px;">
    <div class="service-photo" role="img" aria-label="Hands installing memory into a motherboard" style="background:linear-gradient(135deg,#1e3b5a,#3c8bb3,#c8a58c);"></div>
    <div class="service-label">In-Store Services</div>
  </div>
  <div class="service" style="left:191px;width:156px;">
    <div class="service-photo" role="img" aria-label="Technician with a tablet beside server racks" style="background:linear-gradient(135deg,#1a2a22,#4f6b4a,#c9c0a4);"></div>
    <div class="service-label">On-Site Support</div>
  </div>
  <div class="service" style="left:355px;width:160px;">
    <div class="service-photo" role="img" aria-label="Silhouetted meeting under sketched technology icons" style="background:linear-gradient(180deg,#f2f2f2,#c8c8c8 70%,#2a2a2a);"></div>
    <div class="service-label">Remote Support</div>
  </div>
  <div class="service" style="left:527px;width:160px;">
    <div class="service-photo" role="img" aria-label="Hand holding a phone with glowing wireless icons" style="background:linear-gradient(135deg,#1b2e4a,#4a6f9a,#b8c9dd);"></div>
    <div class="service-label">WiFi Solutions</div>
  </div>

  <div class="abs footer-info">
    <div><svg viewBox="0 0 16 16"><path d="M8 15 C8 15 3 9.5 3 6 A5 5 0 0 1 13 6 C13 9.5 8 15 8 15Z" fill="none" stroke="var(--white)" stroke-width="1.3"/><circle cx="8" cy="6" r="1.8" fill="none" stroke="var(--white)" stroke-width="1.3"/></svg>872 Larkspur Ave. Hudson, IA 50619</div>
    <div><svg viewBox="0 0 16 16"><circle cx="8" cy="8" r="6.5" fill="none" stroke="var(--white)" stroke-width="1.2"/><ellipse cx="8" cy="8" rx="3" ry="6.5" fill="none" stroke="var(--white)" stroke-width="1.2"/><path d="M1.5 8 H14.5 M2.5 4.7 H13.5 M2.5 11.3 H13.5" stroke="var(--white)" stroke-width="1.2"/></svg>www.quillbyrnservices.com</div>
  </div>

  <div class="abs footer-phone">
    <svg viewBox="0 0 44 44"><circle cx="22" cy="22" r="19" fill="none" stroke="var(--white)" stroke-width="3"/><path d="M15 12 L19 12 L21 18 L18 20 C19.5 23.5 21 25 24.5 26.5 L26.5 23.5 L32 25.5 L32 29.5 C32 31 30.5 32 29 32 C20 31 13 24 12 15 C12 13.5 13.5 12 15 12Z" fill="var(--white)"/></svg>
    <span>319-555-0174</span>
  </div>
</section>

</body>
</html>
```